Flyer Design

we need a flyer designing for our independent estate and letting agents based in Gosport Hampshire, our company name is Farrow and Partners Gosport, our contact details are 37 Willowmere Lane, Gosport, Hampshire PO13 4TJ, 02392 784630, email :tamsin@farrowpartners-example.co.uk. Our special offer we'd like to advertise is for the year 2015 we aim to sell 100 properties and only charge £1000 no vat sellers fee for each property sold. We are also offering a free no obligation market appraisal by one of our professional assessors. The flyer must have this disclaimer added to the bottom of it: if you are currently on the market with another agent then your current terms and conditions may need to be reviewed prior to changing agency. We advertise on Homevista and would like to see designs that use the colours lime green and navy blue. The final design should be eye catching and promote this special offer.

```html
<!DOCTYPE html>
<html lang="en">
<head>
<meta charset="utf-8">
<title>Farrow and Partners – Estate &amp; Letting Agents Flyer</title>
<link rel="stylesheet" href="https://fonts.googleapis.com/css2?family=Arimo:wght@400;700&display=swap">
<style>
  :root {
    --sky-blue: #27a7e1;
    --ink: #231f20;
    --lime: #8dc63f;
    --red: #e8373f;
    --red-stamp: #c8202a;
    --charcoal: #333333;
    --divider: #9a9a9a;
    --white: #ffffff;
    --paper: #f4f5f6;
    --blueprint: #dfe3e7;
  }
  * { box-sizing: border-box; margin: 0; padding: 0; }
  html, body { width: 1200px; height: 847px; overflow: hidden; background: var(--white); }
  .flyer {
    position: relative; width: 1200px; height: 847px; overflow: hidden;
    font-family: "Arimo", Arial, sans-serif; background: var(--sky-blue);
  }
  .abs { position: absolute; }

  /* Header */
  .brand-name {
    left: 64px; top: 62px; width: 260px;
    color: var(--white); font-size: 36px; font-weight: 700; line-height: 44px;
  }
  .brand-mark {
    left: 64px; top: 170px; width: 24px; height: 24px; background: var(--white);
  }
  .skyline {
    left: 358px; top: 0; width: 842px; height: 245px;
    background: linear-gradient(to bottom, rgba(10,10,10,0.55) 0%, #0a0a0a 55%, #0a0a0a 100%);
  }
  .contact {
    left: 468px; top: 178px; color: var(--white); font-size: 21.5px; line-height: 34px;
  }

  /* Middle band */
  .hero { left: 0; top: 245px; width: 1200px; height: 330px; background: var(--white); }
  .blueprint {
    left: 495px; top: 245px; width: 705px; height: 330px;
    background: linear-gradient(120deg, var(--paper) 0%, var(--blueprint) 60%, var(--paper) 100%);
  }
  .services {
    left: 22px; top: 258px; font-size: 32.5px; font-weight: 700; white-space: nowrap; letter-spacing: -0.3px;
  }
  .services .sales { color: var(--lime); }
  .services .lettings { color: var(--charcoal); }
  .services .commercial { color: var(--red); }
  .services .sep { color: var(--divider); font-weight: 400; }
  .headline {
    left: 30px; top: 302px; color: var(--red); font-size: 79px; font-weight: 700; line-height: 94px;
    -webkit-text-stroke: 2px #5a1a1c; paint-order: stroke fill; letter-spacing: -0.5px; white-space: nowrap;
  }
  .call {
    left: 20px; top: 506px; color: var(--ink); font-size: 63px; font-weight: 700; letter-spacing: 0.5px; white-space: nowrap;
  }
  .guarantee-badge { left: 940px; top: 310px; }

  /* Offer cards */
  .card { top: 612px; height: 178px; background: var(--white); overflow: hidden; }
  .card-fee { left: 60px; width: 330px; }
  .card-vat { left: 452px; width: 306px; }
  .card-appraisal { left: 820px; width: 307px; }
  .card .wedge { position: absolute; inset: 0; background: var(--lime); }
  .card-fee .wedge { clip-path: polygon(55% 0, 100% 0, 100% 100%, 30% 100%); }
  .card-vat .wedge { clip-path: polygon(50% 0, 100% 0, 100% 100%, 26% 100%); }
  .card-appraisal .wedge { clip-path: polygon(55% 0, 100% 0, 100% 100%, 20% 100%); }
  .card .offer {
    position: absolute; right: 16px; color: var(--white); font-weight: 700; text-align: right;
  }
  .card-fee .offer, .card-vat .offer { top: 14px; font-size: 44px; line-height: 52px; }
  .card-appraisal .offer { right: 6px; top: 38px; font-size: 23px; line-height: 31px; }
  .card .stamp { position: absolute; }

  .disclaimer { left: 30px; top: 800px; color: var(--white); font-size: 15px; white-space: nowrap; }
</style>
</head>
<body>
<main class="flyer">
  <!-- Header -->
  <p class="abs brand-name">Farrow and Partners</p>
  <div class="abs brand-mark"></div>
  <div class="abs skyline" role="img" aria-label="City skyline silhouette"></div>
  <div class="abs contact">
    <p>E-mail : tamsin@farrowpartners-example.co.uk</p>
    <p>Address : 37 Willowmere Lane, Gosport, Hampshire PO13 4TJ</p>
  </div>

  <!-- Hero band -->
  <div class="abs hero"></div>
  <div class="abs blueprint" role="img" aria-label="Faint architectural sketch of a house plan"></div>
  <p class="abs services">
    <span class="sales">RESIDENTIAL SALES</span> <span class="sep">I</span>
    <span class="lettings">RESIDENTIAL LETTINGS</span> <span class="sep">I</span>
    <span class="commercial">COMMERCIAL PROPERTY</span>
  </p>
  <h1 class="abs headline">Let us take care of<br>your next move...</h1>
  <p class="abs call">CALL US : 02392 784630</p>
  <svg class="abs guarantee-badge" width="225" height="225" viewBox="0 0 225 225" role="img" aria-label="Satisfaction guaranteed badge">
    <circle cx="112" cy="112" r="106" fill="none" stroke="var(--ink)" stroke-width="6"/>
    <circle cx="112" cy="112" r="80" fill="none" stroke="var(--ink)" stroke-width="3"/>
  </svg>

  <!-- Offer cards -->
  <section class="abs card card-fee">
    <div class="wedge"></div>
    <svg class="stamp" style="left:8px;top:30px" width="120" height="120" viewBox="0 0 120 120" role="img" aria-label="Special offer stamp">
      <circle cx="60" cy="60" r="54" fill="none" stroke="var(--red-stamp)" stroke-width="5"/>
      <circle cx="60" cy="60" r="40" fill="none" stroke="var(--red-stamp)" stroke-width="2"/>
    </svg>
    <p class="offer">only<br>charge<br>£1000</p>
  </section>

  <section class="abs card card-vat">
    <div class="wedge"></div>
    <svg class="stamp" style="left:8px;top:36px" width="112" height="112" viewBox="0 0 112 112" role="img" aria-label="No fees sticker">
      <circle cx="56" cy="56" r="52" fill="var(--red-stamp)"/>
    </svg>
    <p class="offer">no vat<br>sellers<br>fee</p>
  </section>

  <section class="abs card card-appraisal">
    <div class="wedge"></div>
    <svg class="stamp" style="left:10px;top:20px" width="172" height="64" viewBox="0 0 172 64" role="img" aria-label="Approved stamp">
      <rect x="3" y="3" width="166" height="58" rx="10" fill="none" stroke="var(--red-stamp)" stroke-width="5"/>
    </svg>
    <p class="offer">free<br>no<br>obligation<br>market appraisal</p>
  </section>

  <p class="abs disclaimer">if you are currently on the market with another agent then your current terms and conditions may need to be reviewed prior to changing agency</p>
</main>
</body>
</html>
```